依頼詳細
表面、裏面あります。素材は現在使っているものから、未使用まで提供します。信頼感がでるデザイン希望
記載項目
必要な項目は全てサンプルに記載してあります。
希望イメージ
シンプル 複雑
単色 カラフル
暗い 明るい
日常 高級
遊び心 厳粛
未来的 伝統的
女性的 男性的
希望する色
青系、グレー系
納品ファイル
• 高解像度JPG (.jpg)
• イラストレーター形式 (.ai)
補足説明
イラストレーターはバージョン10でお願いします
カラーはRGBとCMYK両方
電話番号を大きく表示願います!

色の使い方にメリハリがあり、気に入りました

こちらからラフスケッチを提供しているので、方向性は概ねずれないので、後は色使いとか、気の利いたレイアウトに期待していました。
ご参加のみなさまありがとうございました

```html
<!DOCTYPE html>
<html lang="ja">
<head>
<meta charset="utf-8">
<title>スカイウイング飛行学校 名刺デザイン</title>
<link rel="stylesheet" href="https://fonts.googleapis.com/css2?family=Noto+Sans+JP:wght@400;700;900&family=Noto+Serif+JP:wght@500;700&display=swap">
<style>
:root{
  --navy:#1b2f86;
  --blue:#2a4fc4;
  --sky:#5aa6e8;
  --pale:#e3eefa;
  --grey:#8d96a8;
  --light-grey:#e6e8ee;
  --red:#e0101a;
  --yellow:#fff35a;
  --orange:#f39a1e;
  --ink:#222a3c;
  --white:#ffffff;
}
*{margin:0;padding:0;box-sizing:border-box}
html,body{width:783px;height:1200px;overflow:hidden;background:var(--white)}
body{position:relative;font-family:"Noto Sans JP",sans-serif;color:var(--ink)}
.card{position:absolute;width:710px;height:258px;background:linear-gradient(180deg,var(--white) 60%,var(--pale) 100%);border:1px solid #c9cfdb;box-shadow:2px 3px 6px rgba(0,0,0,.18);overflow:hidden}
.card--a{left:21px}
.card--b{left:52px}
.card--1{top:13px}
.card--2{top:303px}
.card--3{top:598px}
.card--4{top:893px}
.band{position:absolute;left:0;top:0;width:100%;height:40px;display:flex;align-items:center;justify-content:center;font-family:"Noto Serif JP",serif;font-weight:700;font-size:22px;color:var(--white);letter-spacing:1px}
.band--blue{background:linear-gradient(90deg,var(--navy),var(--blue) 45%,var(--sky) 80%,var(--white))}
.band--grey{background:linear-gradient(90deg,var(--navy),var(--grey) 50%,var(--light-grey))}
.brand{position:absolute;left:26px;top:56px;width:200px;text-align:center}
.brand__mark{width:34px;height:34px;border-radius:50%;background:var(--blue);margin:0 auto 8px}
.brand__name{font-weight:900;font-size:20px;line-height:1.15;color:var(--navy)}
.brand__url{font-size:11px;color:var(--navy);margin-top:6px}
.tel{position:absolute;left:26px;bottom:10px;font-size:24px;line-height:1.2;font-weight:700;color:var(--navy);letter-spacing:1px}
.tel--back{font-size:22px}
.lead{position:absolute;left:250px;top:44px;width:430px;text-align:center}
.lead__sub{font-size:15px;line-height:1.3;font-weight:700;color:var(--red)}
.lead__main{display:inline-block;font-size:24px;line-height:1.3;font-weight:900;color:var(--red);background:linear-gradient(transparent 55%,var(--yellow) 55%);padding:0 4px}
.points{position:absolute;list-style:none;font-weight:700;color:var(--ink)}
.points li{display:flex;align-items:center;gap:6px}
.points li::before{content:"";width:14px;height:14px;background:var(--red);flex:none}
.points--front{left:262px;top:100px;font-size:17px;line-height:1.38}
.points--back{left:120px;top:96px;font-size:16px;line-height:1.35}
.points .boxed{background:var(--light-grey);padding:0 6px 0 2px;font-size:15px}
.points .alert{color:var(--red)}
.address{position:absolute;bottom:10px;font-size:10px;line-height:1.45;color:#4a5163}
.address--front{left:320px}
.address--back{left:330px}
.promo{position:absolute;left:22px;top:42px;font-weight:900;font-size:28px;line-height:1.4;color:var(--red);transform:rotate(-8deg)}
.fee{position:absolute;left:26px;top:188px;padding:2px 12px;font-weight:900;font-size:18px;line-height:1.45}
.fee--light{background:var(--pale);color:var(--orange);border:2px solid var(--sky)}
.fee--bold{background:var(--red);color:var(--white);border:2px solid var(--red)}
</style>
</head>
<body>

<section class="card card--a card--1">
  <div class="band band--blue">スカイウイング飛行学校</div>
  <div class="brand">
    <div class="brand__mark"></div>
    <div class="brand__name">Sky Wing<br>Flight School</div>
    <div class="brand__url">skywing-fs.jp</div>
  </div>
  <div class="lead">
    <div class="lead__sub">東海地区で唯一の</div>
    <div class="lead__main">ドローンフライト講習スタート!!</div>
  </div>
  <ul class="points points--front">
    <li>練習用ドローン完備</li>
    <li>広大なフライト環境</li>
    <li>確かなカリキュラム</li>
    <li><span class="boxed">申請に役立つ機体証明書の発行</span></li>
  </ul>
  <div class="tel">TEL 052-480-1736</div>
  <div class="address address--front">岐阜県各務原市見本町1-2-3<br>スカイウイング飛行学校 本部<br>info@skywing-fs.jp</div>
</section>

<section class="card card--a card--2">
  <div class="band band--blue">ドローン飛行許可申請作成代行サービス</div>
  <div class="promo">プロがお助け!!</div>
  <ul class="points points--back">
    <li>書類の作り方を調べる手間をカット</li>
    <li>20ページ以上に及ぶ申請書を一括作成</li>
    <li>イベント、年間許可等、実績多数!</li>
    <li class="alert">責任とビジネス最適な申請方法を提案します。</li>
  </ul>
  <div class="fee fee--light">制作費用4万円~</div>
  <div class="tel tel--back">TEL 052-480-1736</div>
  <div class="address address--back">岐阜県各務原市見本町1-2-3<br>スカイウイング飛行学校 本部<br>info@skywing-fs.jp</div>
</section>

<section class="card card--b card--3">
  <div class="band band--grey">スカイウイング飛行学校</div>
  <div class="brand">
    <div class="brand__mark"></div>
    <div class="brand__name">Sky Wing<br>Flight School</div>
    <div class="brand__url">skywing-fs.jp</div>
  </div>
  <div class="lead">
    <div class="lead__sub">東海地区で唯一の</div>
    <div class="lead__main">ドローンフライト講習スタート!!</div>
  </div>
  <ul class="points points--front">
    <li>練習用ドローン完備</li>
    <li>広大なフライト環境</li>
    <li>確かなカリキュラム</li>
    <li><span class="boxed">申請に役立つ機体証明書の発行</span></li>
  </ul>
  <div class="tel">TEL 052-480-1736</div>
  <div class="address address--front">岐阜県各務原市見本町1-2-3<br>スカイウイング飛行学校 本部<br>info@skywing-fs.jp</div>
</section>

<section class="card card--b card--4">
  <div class="band band--grey">ドローン飛行許可申請作成代行サービス</div>
  <div class="promo">プロがお助け!!</div>
  <ul class="points points--back">
    <li>書類の作り方を調べる手間をカット</li>
    <li>20ページ以上に及ぶ申請書を一括作成</li>
    <li>イベント、年間許可等、実績多数!</li>
    <li class="alert">責任とビジネス最適な申請方法を提案します。</li>
  </ul>
  <div class="fee fee--bold">制作費用4万円~</div>
  <div class="tel tel--back">TEL 052-480-1736</div>
  <div class="address address--back">岐阜県各務原市見本町1-2-3<br>スカイウイング飛行学校 本部<br>info@skywing-fs.jp</div>
</section>

</body>
</html>
```